Business card design

Hi,
I need to have a business card design based on the current logo.
If competitive I not put it out to everyone.

It can be single of double sided

Target Market(s)

Food businesses

Industry/Entity Type

Food Manufacturing

Contact Information for Business Card

Details will on card will be as follows Name = Marcus Helt Email = Marcus@TalBakery.com.au Phone = 0418562207 Address = 17 Lanford Street , Fortitude Valley QLD 4006 Australia

Font styles to use
Other font styles liked:
• based on two fonts - Adelle & Museo

Requirements
Must have
• Based on the on switch concept

```html
<!DOCTYPE html>
<html lang="en">
<head>
<meta charset="utf-8">
<title>TalBakery Business Card</title>
<link rel="stylesheet" href="https://fonts.googleapis.com/css2?family=Crimson+Text:wght@400&family=Mukta:wght@500&display=swap">
<style>
  :root {
    --backdrop: #949494;
    --card-base: #fbfaf9;
    --card-tint: #efebe8;
    --brand-red: #ee2f4a;
    --panel-top: #e8304a;
    --panel-bottom: #3a1527;
    --ink-dark: #3a2a2e;
    --ink-light: #ffffff;
    --serif: "Crimson Text", Georgia, serif;
    --sans: "Mukta", Arial, sans-serif;
  }
  html, body {
    margin: 0;
    padding: 0;
    width: 1200px;
    height: 1000px;
    overflow: hidden;
    background: var(--backdrop);
  }
  .card {
    position: absolute;
    left: 142px;
    top: 233px;
    width: 916px;
    height: 522px;
    overflow: hidden;
  }
  .card-art {
    position: absolute;
    inset: 0;
  }
  .holder-name {
    position: absolute;
    left: 37px;
    top: 52px;
    margin: 0;
    font-family: var(--serif);
    font-weight: 400;
    font-size: 46px;
    line-height: 1;
    color: var(--ink-dark);
  }
  .contact-list {
    position: absolute;
    left: 66px;
    top: 190px;
    margin: 0;
    padding: 0;
    list-style: none;
    font-family: var(--serif);
    font-size: 19px;
    line-height: 20px;
    color: var(--ink-light);
  }
  .contact-item {
    position: absolute;
    left: 0;
    display: flex;
    align-items: flex-start;
    white-space: nowrap;
  }
  .contact-item svg {
    width: 20px;
    height: 20px;
    margin-right: 14px;
    flex: none;
  }
  .contact-phone { top: 0; }
  .contact-email { top: 58px; }
  .contact-address { top: 116px; }
  .brand {
    position: absolute;
    right: 33px;
    top: 198px;
    text-align: right;
    color: var(--ink-dark);
  }
  .brand-name {
    display: flex;
    align-items: center;
    justify-content: flex-end;
    font-family: var(--sans);
    font-weight: 500;
    font-size: 60px;
    line-height: 60px;
    letter-spacing: 1px;
  }
  .brand-dot {
    width: 26px;
    height: 26px;
    border-radius: 50%;
    background: var(--brand-red);
    margin-right: 18px;
  }
  .brand-tagline {
    font-family: var(--sans);
    font-weight: 500;
    font-size: 18px;
    line-height: 22px;
    margin-top: 4px;
  }
  .band-email {
    position: absolute;
    left: 512px;
    right: 0;
    top: 424px;
    text-align: center;
    font-family: var(--serif);
    font-size: 23px;
    line-height: 30px;
    color: var(--ink-light);
  }
</style>
</head>
<body>
  <section class="card">
    <svg class="card-art" width="916" height="522" viewBox="0 0 916 522">
      <defs>
        <linearGradient id="pattern-tone" x1="0" y1="0" x2="1" y2="1">
          <stop offset="0" stop-color="var(--card-base)"/>
          <stop offset="1" stop-color="var(--card-tint)"/>
        </linearGradient>
        <linearGradient id="panel-tone" x1="0" y1="0" x2="0" y2="1">
          <stop offset="0" stop-color="var(--panel-top)"/>
          <stop offset="1" stop-color="var(--panel-bottom)"/>
        </linearGradient>
      </defs>
      <rect class="food-pattern" width="916" height="522" fill="url(#pattern-tone)" role="img" aria-label="Faint hand-drawn pattern of plates of pasta, cutlery, cheese, eggs and mushrooms"/>
      <path class="contact-panel" d="M0,127 H275 Q310,127 330,160 L505,448 Q515,470 540,470 H0 Z" fill="url(#panel-tone)"/>
      <path class="email-band" d="M916,410 H515 Q493,410 500,432 L522,470 H916 Z" fill="var(--brand-red)"/>
    </svg>

    <h1 class="holder-name">Marcus Helt</h1>

    <ul class="contact-list">
      <li class="contact-item contact-phone">
        <svg viewBox="0 0 20 20"><circle cx="10" cy="10" r="10" fill="#2b1a20"/><path d="M5.5 9.5h9l-1-2.5h-7z M7 10.5h6v3.5H7z" fill="#fff"/></svg>
        <span>0418562207</span>
      </li>
      <li class="contact-item contact-email">
        <svg viewBox="0 0 20 20"><circle cx="10" cy="10" r="10" fill="#2b1a20"/><rect x="5.5" y="7" width="9" height="6.5" fill="#fff"/><path d="M5.5 7l4.5 3.5L14.5 7" fill="none" stroke="#2b1a20" stroke-width="1"/></svg>
        <span>Marcus@TalBakery.com.au</span>
      </li>
      <li class="contact-item contact-address">
        <svg viewBox="0 0 20 20"><circle cx="10" cy="10" r="10" fill="#2b1a20"/><path d="M10 4.5a3.8 3.8 0 0 0-3.8 3.8c0 2.8 3.8 7 3.8 7s3.8-4.2 3.8-7A3.8 3.8 0 0 0 10 4.5z" fill="#fff"/><circle cx="10" cy="8.3" r="1.4" fill="#2b1a20"/></svg>
        <span>17 Lanford Street , Har-<br>low Heights QLD 4127<br>Australia</span>
      </li>
    </ul>

    <div class="brand">
      <div class="brand-name"><span class="brand-dot"></span>TALBAKERY</div>
      <div class="brand-tagline">Fresh Bakes On Request</div>
    </div>

    <div class="band-email">Marcus@TalBakery.com.au</div>
  </section>
</body>
</html>
```